Postcard double sided

Title: DWIGHT'S REVENGE

Why would Dwight Kessler align himself with Gordon Pruett?

(photo of two guys)

Dwight approached elected officials that he wanted to run for office, but did not have money to finance his campaign. He wanted other elected officials to finance his campaign. Everyone told him that they would help him get the vote out, but that he needed to finance his own race.

In comes Gordon Pruett.

Gordon Pruett who has a pay to play scheme over at the City, told Dwight he would finance his campaign on one condition.

He needed to run against Steven Hulse.

Why would Dwight want to run with no money?

Backside

DWIGHT'S REVENGE

Dwight decided to run because no one on the school board would terminate Dwight's ex and her new boyfriend who both work for the school district. His ex even filed criminal charges against him that are still pending.

Mug Shot facing left (name the charges Criminal Trespass , and Criminal Mischief (highlight bold letters use two lines) mug shot facing right

Complaint one (then photo with full face) Compliant 2)
(showcharges)

Dwight's ultimate goal is to terminate his ex and her new boyfriend if elected.
Plus Gordon Pruett needs the majority on the school board to do what he does bet.

Kickbacks for Contracts.

They will hire their own contractors!
Say "No" to Dwight's Revenge and Gordon Pruett Money Grab!

Title On Back: all caps: DOMESTIC VIOLENCE

```html
<!DOCTYPE html>
<html lang="en">
<head>
<meta charset="utf-8">
<title>Dwight's Revenge – Postcard</title>
<link rel="stylesheet" href="https://fonts.googleapis.com/css2?family=Alfa+Slab+One&family=Kaushan+Script&family=Roboto:ital,wght@0,400;0,500;0,700;1,700;1,900&display=swap">
<style>
  :root{
    --navy:#1b3c6e;
    --sky:#62c6f0;
    --white:#ffffff;
    --page:#f1f1f1;
    --ink:#1f3f73;
    --line:#444444;
  }
  *{box-sizing:border-box;margin:0;padding:0}
  html,body{width:937px;height:1200px;overflow:hidden;background:var(--page)}
  body{position:relative;font-family:"Roboto",Arial,sans-serif}
  .card{
    position:absolute;left:54.5px;width:828px;height:592px;
    transform:scale(.963);transform-origin:center top;
    overflow:hidden;box-shadow:0 2px 8px rgba(0,0,0,.15);
  }
  .card--back{top:20px;background:var(--white)}
  .card--front{top:610px;background:var(--sky)}
  .abs{position:absolute}

  /* back side */
  .back-title{left:49px;top:44px;font-family:"Alfa Slab One",Georgia,serif;font-size:31px;color:var(--navy);letter-spacing:-.5px;line-height:1}
  .back-intro{left:49px;top:84px;width:268px;font-size:14.4px;line-height:17.8px;color:var(--ink)}
  .mug-strip{left:49px;top:198px;width:265px;height:107px;display:flex;gap:3px}
  .mug-photo{flex:1;background:linear-gradient(180deg,#8a8f93 0%,#6c7074 60%,#2f4a3a 100%)}
  .charges-bar{left:49px;top:305px;width:265px;height:26px;background:var(--sky);color:var(--navy);font-size:12.8px;font-weight:700;text-align:center;line-height:26px}
  .back-goal{left:49px;top:352px;width:270px;font-size:14.4px;line-height:17.8px;color:var(--ink)}
  .back-goal b{font-weight:700;color:var(--navy)}
  .call-box{left:49px;top:461px;width:266px;height:82px;background:var(--navy);color:var(--white);text-align:center;font-size:14.2px;line-height:19.5px;padding-top:11px}
  .call-box b{font-weight:700}
  .hl{color:var(--sky)}
  .stamp-box{left:668px;top:51px;width:112px;height:118px;border:1.5px solid var(--line)}
  .address-line{left:364px;width:415px;height:0;border-top:1.5px solid var(--line)}
  .indicia-box{left:364px;top:425px;width:415px;height:119px;border:1.5px solid var(--line);display:flex;align-items:center;justify-content:center;font-size:18px;color:#222}

  /* front side */
  .front-title{left:0;top:0}
  .front-sub{right:48px;top:114px;text-align:right;font-size:25px;font-weight:700;font-style:italic;line-height:31px;color:var(--white)}
  .front-sub span{color:var(--navy)}
  .duo-photo{left:0;top:106px;width:368px;height:390px;background:linear-gradient(180deg,#62c6f0 0%,#3f5266 35%,#1f2a3a 100%)}
  .story-box{left:385px;top:188px;width:443px;height:146px;background:var(--navy);color:var(--white);font-size:15.3px;line-height:19.8px;padding:12px 14px 0 20px}
  .story-box b{color:var(--sky);font-weight:700}
  .enter{left:393px;top:353px;color:var(--navy);font-size:17px;line-height:21px}
  .enter-name{left:393px;top:372px;font-family:"Kaushan Script",cursive;font-size:27px;color:var(--white)}
  .enter-need{left:393px;top:414px;color:var(--navy);font-size:17px;line-height:21px}
  .enter-need b{font-weight:700}
  .band{left:0;top:0}
  .band-text{left:49px;top:500px;width:520px;color:var(--white);font-size:17px;line-height:22px}
  .band-text b{color:var(--sky);font-weight:700}
  .seal{left:588px;top:366px;width:190px;height:190px;border-radius:50%;background:var(--white);text-align:center;color:var(--navy)}
  .seal-top{margin-top:30px;font-size:21px;line-height:24px}
  .seal-name{font-family:"Alfa Slab One",Georgia,serif;font-size:40px;line-height:46px;letter-spacing:-1px}
  .seal-mid{font-size:20px;line-height:23px}
  .seal-end{font-family:"Alfa Slab One",Georgia,serif;font-size:22px;line-height:28px}
</style>
</head>
<body>

<section class="card card--back" aria-label="Postcard back">
  <h2 class="abs back-title">DWIGHT'S REVENGE</h2>
  <p class="abs back-intro">Dwight decided to run because no one on the school board would terminate Dwight's ex and her new boyfriend who both work for the school district. His ex even filed criminal charges against him that are still pending.</p>
  <div class="abs mug-strip">
    <div class="mug-photo" role="img" aria-label="Booking photo, left profile"></div>
    <div class="mug-photo" role="img" aria-label="Booking photo, front view"></div>
    <div class="mug-photo" role="img" aria-label="Booking photo, right profile"></div>
  </div>
  <div class="abs charges-bar">Criminal Trespass , and Criminal Mischief</div>
  <p class="abs back-goal">Dwight's ultimate goal is to terminate his ex and her new boyfriend if elected. <b>Plus Gordon Pruett needs the majority on the school board to do what he does bet.</b></p>
  <div class="abs call-box">They will hire their own contractors!<br><b>Say "No" to <span class="hl">Dwight's Revenge and<br>Gordon Pruett Money Grab!</span></b></div>

  <div class="abs stamp-box"></div>
  <div class="abs address-line" style="top:247px"></div>
  <div class="abs address-line" style="top:297px"></div>
  <div class="abs address-line" style="top:347px"></div>
  <div class="abs indicia-box">1 INCH X 3.5 INCH</div>
</section>

<section class="card card--front" aria-label="Postcard front">
  <div class="abs duo-photo" role="img" aria-label="Photo of Dwight Kessler and Gordon Pruett standing together in suits"></div>

  <svg class="abs front-title" width="828" height="112" viewBox="0 0 828 112">
    <text x="50" y="103" textLength="731" lengthAdjust="spacingAndGlyphs" font-family="'Alfa Slab One', Georgia, serif" font-size="92" fill="#1b3c6e">DWIGHT'S REVENGE</text>
  </svg>
  <p class="abs front-sub">Why would Dwight Kessler align himself with<br><span>Gordon Pruett?</span></p>

  <div class="abs story-box"><b>Dwight approached elected officials</b> that he wanted to run for office, but did not have money to finance his campaign. He wanted other <b>elected officials</b> to finance his campaign. Everyone told him that they would help him get the vote out, but that <b>he needed to finance his own race.</b></div>

  <p class="abs enter">In comes</p>
  <p class="abs enter-name">Gordon Pruett</p>
  <p class="abs enter-need">He needed to run<br>against <b>Steven Hulse.</b></p>

  <svg class="abs band" width="828" height="592" viewBox="0 0 828 592">
    <path d="M0 488 C 230 470, 520 478, 828 412 L828 592 L0 592 Z" fill="#1b3c6e"/>
  </svg>
  <p class="abs band-text"><b>Gordon Pruett</b> who has a pay to play scheme over at the City, told Dwight <b>he would finance his campaign on one condition.</b></p>

  <div class="abs seal">
    <p class="seal-top">Why would</p>
    <p class="seal-name">DWIGHT</p>
    <p class="seal-mid">want to run with</p>
    <p class="seal-end">NO MONEY?</p>
  </div>
</section>

</body>
</html>
```